Uprising SaaS company needs an attractive business card design

We're an uprising SaaS company who's attempting to attack the rigid car (insurance) claims management market in Europe.
We want to our mighty base order management system, listen to our clients to connect the smart ideas to build something even mightier.
We primarily focus on helping our customers manage their customers' claims/orders and get them resolved as smoothly as possible.
We'd like the business card design to express technical innovation and the fact that we connect smart ideas, as our company slogan indicates.
Contact Information for Business Card
Name, position, website, email, mobile, business address
Font styles to use
Colors
Designer to choose colors to be used in the design.
Look and feel
Each slider illustrates characteristics of the customer's brand and the style your logo design should communicate.

```html
<!DOCTYPE html>
<html lang="en">
<head>
<meta charset="UTF-8">
<title>Veloqent Business Card</title>
<link rel="stylesheet" href="https://fonts.googleapis.com/css2?family=Montserrat:wght@400;500;700&display=swap">
<style>
  :root {
    --backdrop: #d0d0d0;
    --card-front: #ffffff;
    --card-back: #808080;
    --ink: #7a7a7a;
    --ink-soft: #8a8a8a;
    --accent: #7ccbe0;
    --white: #ffffff;
  }
  * { margin: 0; padding: 0; box-sizing: border-box; }
  html, body {
    width: 1000px; height: 1200px; overflow: hidden;
    background: var(--backdrop);
    font-family: "Montserrat", sans-serif;
  }
  .canvas { position: relative; width: 1000px; height: 1200px; }
  .card {
    position: absolute; left: 135px; width: 730px; height: 418px;
    border-radius: 30px; overflow: hidden;
  }
  .card--front { top: 160px; background: var(--card-front); }
  .card--back { top: 622px; background: var(--card-back); }

  .wordmark {
    position: absolute; font-weight: 400; letter-spacing: 1px; line-height: 1;
  }
  .card--front .wordmark {
    right: 60px; top: 58px; font-size: 80px; color: var(--ink);
  }
  .card--back .wordmark {
    left: 0; right: 0; top: 168px; text-align: center;
    font-size: 118px; color: var(--white);
  }
  .wordmark-dot {
    display: inline-block; width: 16px; height: 16px; border-radius: 50%;
    background: var(--accent); margin-left: 10px; vertical-align: top; margin-top: 6px;
  }
  .card--front .wordmark-dot { width: 12px; height: 12px; margin-left: 8px; }

  .holder { position: absolute; left: 58px; top: 202px; }
  .holder-name { font-size: 26px; font-weight: 700; color: var(--ink); }
  .holder-role { font-size: 17px; font-weight: 400; color: var(--ink-soft); margin-top: 6px; }

  .divider { position: absolute; left: 58px; top: 284px; width: 612px; height: 2px; }

  .contacts { position: absolute; left: 58px; top: 306px; list-style: none; }
  .contacts li {
    display: flex; align-items: center; height: 25px;
    font-size: 18px; color: var(--ink-soft);
  }
  .contacts svg { width: 14px; height: 14px; margin: 0 14px 0 2px; fill: var(--ink-soft); }

  .address {
    position: absolute; left: 513px; top: 303px;
    font-size: 18px; line-height: 25px; color: var(--ink-soft); font-style: normal;
  }
</style>
</head>
<body>
<main class="canvas">
  <section class="card card--front">
    <div class="wordmark">veloqent<span class="wordmark-dot"></span></div>

    <div class="holder">
      <p class="holder-name">Marten Holloway</p>
      <p class="holder-role">Managing Director</p>
    </div>

    <svg class="divider" viewBox="0 0 612 2" preserveAspectRatio="none">
      <defs>
        <linearGradient id="divider-fade" x1="0" x2="1">
          <stop offset="0" stop-color="#8a8a8a"/>
          <stop offset="1" stop-color="#7ccbe0"/>
        </linearGradient>
      </defs>
      <line x1="0" y1="1" x2="612" y2="1" stroke="url(#divider-fade)" stroke-width="1.2" stroke-dasharray="4 2"/>
    </svg>

    <ul class="contacts">
      <li>
        <svg viewBox="0 0 24 24"><path d="M6.6 10.8a15 15 0 0 0 6.6 6.6l2.2-2.2a1 1 0 0 1 1-.25 11.4 11.4 0 0 0 3.6.57 1 1 0 0 1 1 1V20a1 1 0 0 1-1 1A17 17 0 0 1 3 4a1 1 0 0 1 1-1h3.5a1 1 0 0 1 1 1c0 1.25.2 2.45.57 3.6a1 1 0 0 1-.25 1z"/></svg>
        1-800-555-0142
      </li>
      <li>
        <svg viewBox="0 0 24 24"><path d="M2 5h20v14H2z M2 5l10 8 10-8" fill="none" stroke="#8a8a8a" stroke-width="2"/><path d="M3 6l9 7 9-7v13H3z"/></svg>
        hello@veloqent.com
      </li>
      <li>
        <svg viewBox="0 0 24 24"><g fill="none" stroke="#8a8a8a" stroke-width="2"><circle cx="12" cy="12" r="9.5"/><ellipse cx="12" cy="12" rx="4" ry="9.5"/><line x1="2.5" y1="12" x2="21.5" y2="12"/></g></svg>
        www.veloqent.com
      </li>
    </ul>

    <address class="address">
      4200 Larkfield Ave<br>
      Cedar Hollow<br>
      Minnesota(MN)
    </address>
  </section>

  <section class="card card--back">
    <div class="wordmark">veloqent<span class="wordmark-dot"></span></div>
  </section>
</main>
</body>
</html>
```